Dental promotion

We are a family dental office that provides 99% of the dental service for the entire family, including IV sedation, wisdom teeth extraction, implant, Clearvanta, root canal, teeth whiting et cl. We currently have promotion for Clearvanta, implant and new patients who don’t have insurance. 1500 off Clearvanta, 2000 off for implant, 98 dollars for new patient that cover exam, x-ray, and regular cleaning. We also offer financing option.
More information please check our website
https://www.brookhollowfamilydentistry.example/

```html
<!DOCTYPE html>
<html lang="en">
<head>
<meta charset="utf-8">
<title>Brookhollow Family Dentistry – Promotional Postcard</title>
<link rel="stylesheet" href="https://fonts.googleapis.com/css2?family=Exo+2:wght@700;800;900&family=Barlow:wght@400;500;600;700&family=Comfortaa:wght@400;700&display=swap">
<style>
:root{
  --green:#5cb533;
  --green-light:#8cc63f;
  --green-dark:#3f9a2c;
  --navy:#23287a;
  --navy-mid:#2e3192;
  --ink:#1f1f2e;
  --white:#ffffff;
  --stamp:#ececec;
  --table:#e8e8e6;
  --photo-a:#d9e6ee;
  --photo-b:#b9ccd8;
}
*{margin:0;padding:0;box-sizing:border-box}
html,body{width:1200px;height:911px;overflow:hidden}
body{background:var(--table);font-family:"Barlow",sans-serif;color:var(--ink);position:relative}
.card{position:absolute;left:285px;width:630px;height:420px;background:var(--white);overflow:hidden;box-shadow:0 6px 18px rgba(0,0,0,.18)}
.card--back{top:24px}
.card--front{top:467px}
.card svg.shapes{position:absolute;inset:0;width:100%;height:100%}
.abs{position:absolute}

/* back side */
.offers{left:20px;top:20px;width:215px;list-style:none;font-family:"Comfortaa",sans-serif;color:var(--white);font-size:10px;line-height:1.15}
.offers li{position:relative;padding-left:14px;margin-bottom:11px}
.offers li::before{content:"";position:absolute;left:0;top:1px;width:9px;height:9px;border-radius:50%;background:var(--white)}
.offers li::after{content:"";position:absolute;left:2.5px;top:3px;width:4px;height:2.5px;border-left:1.5px solid var(--green);border-bottom:1.5px solid var(--green);transform:rotate(-45deg)}
.offers b{font-weight:700}
.services-title{left:0;top:145px;width:143px;height:24px;background:var(--navy);border-radius:0 12px 12px 0;color:var(--white);font-family:"Barlow",sans-serif;font-weight:600;font-size:16px;line-height:24px;padding-left:20px;letter-spacing:.3px}
.services{left:10px;top:184px;width:260px;display:grid;grid-template-columns:repeat(3,84px);row-gap:6px}
.service{display:flex;flex-direction:column;align-items:center;color:var(--white);font-family:"Barlow",sans-serif;font-weight:600;font-size:9px;line-height:1.1;text-align:center;height:70px;text-transform:uppercase}
.service svg{width:46px;height:46px;margin-bottom:3px}
.book{font-family:"Barlow",sans-serif;font-weight:600;color:var(--white);text-transform:uppercase;white-space:nowrap}
.card--back .book{left:20px;top:340px;font-size:8.5px}
.phone{display:flex;align-items:center;gap:6px;border:1.2px solid var(--white);border-radius:0 12px 12px 0;border-left:none;padding:0 10px 0 0;color:var(--white);font-family:"Exo 2",sans-serif;font-weight:800;white-space:nowrap}
.phone svg{width:18px;height:18px}
.card--back .phone{left:20px;top:352px;height:21px;font-size:19px}
.contact{display:flex;align-items:center;gap:5px;color:var(--white);font-family:"Barlow",sans-serif;font-weight:600;font-size:8.5px;white-space:nowrap}
.dot{width:10px;height:10px;border-radius:50%;background:var(--white);flex:none;position:relative}
.dot::after{content:"";position:absolute;inset:3px;border-radius:50%;background:var(--navy)}
.card--back .c1{left:20px;top:381px}
.card--back .c2{left:20px;top:395px}
.photo{border-radius:50%;border:4px solid var(--white)}
.card--back .photo{left:256px;top:140px;width:134px;height:134px;background:radial-gradient(circle at 40% 40%,var(--photo-a),var(--photo-b))}
.brand{display:flex;align-items:center;gap:6px;color:var(--navy-mid);font-family:"Barlow",sans-serif;font-weight:700;letter-spacing:.6px}
.brand .mark{border:2px solid var(--navy-mid);border-radius:50%;flex:none}
.card--back .brand{left:322px;top:28px;font-size:9px}
.card--back .brand .mark{width:20px;height:20px}
.return{left:322px;top:54px;font-family:"Comfortaa",sans-serif;font-size:8px;line-height:1.35;color:var(--ink)}
.stamp{left:565px;top:20px;width:44px;height:52px;border-radius:5px;background:var(--stamp)}

/* front side */
.card--front .brand{right:20px;top:44px;font-size:19px;letter-spacing:1px;line-height:1.2}
.card--front .brand .mark{width:46px;height:46px;border-width:3px}
.headline{right:21px;top:118px;text-align:right;font-family:"Exo 2",sans-serif;font-weight:900;font-size:28px;line-height:1;text-transform:uppercase}
.headline span{display:block}
.headline .g{color:var(--green-dark)}
.headline .n{color:var(--navy-mid)}
.intro{right:21px;top:206px;width:260px;text-align:right;font-weight:400;font-size:14.5px;line-height:1.22;color:var(--ink)}
.intro em{color:var(--green-dark);font-weight:700}
.card--front .doctor{left:224px;top:256px;width:146px;height:146px;background:radial-gradient(circle at 50% 40%,#e9e3d8,#b9b7ae)}
.card--front .book{left:20px;top:365px;font-size:9.5px}
.card--front .phone{left:20px;top:377px;height:23px;font-size:21px}
.card--front .contact{right:20px;justify-content:flex-end}
.card--front .c1{top:363px}
.card--front .c2{top:378px}
.card--front .c3{top:392px}
</style>
</head>
<body>

<section class="card card--back" aria-label="Postcard back">
  <svg class="shapes" viewBox="0 0 945 630" preserveAspectRatio="none" aria-hidden="true">
    <defs>
      <linearGradient id="back-green" x1="0" y1="0" x2="1" y2="1">
        <stop offset="0" stop-color="#5cb533"/><stop offset="1" stop-color="#8cc63f"/>
      </linearGradient>
    </defs>
    <path d="M370 0 C450 70 490 180 488 300 C486 420 450 530 405 630 H450 C500 520 530 410 525 300 C520 180 480 70 420 0Z" fill="#23287a"/>
    <path d="M0 0 H370 C440 80 475 190 472 300 C468 420 430 530 385 630 H0Z" fill="url(#back-green)"/>
  </svg>

  <ul class="abs offers">
    <li>Clearvanta, implant and new<br>patients who don't have insurance.</li>
    <li><b>1500 off</b> Clearvanta, <b>2000 off</b> for<br>implant.</li>
    <li><b>$98</b> for new patient that cover<br>exam, x-ray, &amp; regular cleaning.</li>
    <li>We also offer <b>financing</b> option.</li>
  </ul>

  <h2 class="abs services-title">OUR SERVICES</h2>
  <div class="abs services">
    <div class="service"><svg viewBox="0 0 48 48"><path d="M8 6C14 2 20 4 24 7C28 4 34 2 40 6C46 12 44 24 40 32C37 40 34 46 31 46C28 46 28 36 24 34C20 36 20 46 17 46C14 46 11 40 8 32C4 24 2 12 8 6Z" fill="#23287a"/></svg>IV<br>Sedation</div>
    <div class="service"><svg viewBox="0 0 48 48"><path d="M8 6C14 2 20 4 24 7C28 4 34 2 40 6C46 12 44 24 40 32C37 40 34 46 31 46C28 46 28 36 24 34C20 36 20 46 17 46C14 46 11 40 8 32C4 24 2 12 8 6Z" fill="#23287a"/></svg>Wisdom teeth<br>extraction</div>
    <div class="service"><svg viewBox="0 0 48 48"><path d="M8 6C14 2 20 4 24 7C28 4 34 2 40 6C46 12 44 24 40 32C37 40 34 46 31 46C28 46 28 36 24 34C20 36 20 46 17 46C14 46 11 40 8 32C4 24 2 12 8 6Z" fill="#23287a"/></svg>Implant</div>
    <div class="service"><svg viewBox="0 0 48 48"><path d="M8 6C14 2 20 4 24 7C28 4 34 2 40 6C46 12 44 24 40 32C37 40 34 46 31 46C28 46 28 36 24 34C20 36 20 46 17 46C14 46 11 40 8 32C4 24 2 12 8 6Z" fill="#23287a"/></svg>Clearvanta</div>
    <div class="service"><svg viewBox="0 0 48 48"><path d="M8 6C14 2 20 4 24 7C28 4 34 2 40 6C46 12 44 24 40 32C37 40 34 46 31 46C28 46 28 36 24 34C20 36 20 46 17 46C14 46 11 40 8 32C4 24 2 12 8 6Z" fill="#23287a"/></svg>Root canal</div>
    <div class="service"><svg viewBox="0 0 48 48"><path d="M8 6C14 2 20 4 24 7C28 4 34 2 40 6C46 12 44 24 40 32C37 40 34 46 31 46C28 46 28 36 24 34C20 36 20 46 17 46C14 46 11 40 8 32C4 24 2 12 8 6Z" fill="#23287a"/></svg>Teeth whiting</div>
  </div>

  <p class="abs book">Book your next dental appointment</p>
  <p class="abs phone"><svg viewBox="0 0 24 24"><path d="M6.6 10.8a15 15 0 006.6 6.6l2.2-2.2c.3-.3.7-.4 1-.2 1.1.4 2.3.6 3.6.6.6 0 1 .4 1 1V20c0 .6-.4 1-1 1C10.6 21 3 13.4 3 4c0-.6.4-1 1-1h3.5c.6 0 1 .4 1 1 0 1.3.2 2.5.6 3.6.1.3 0 .7-.2 1z" fill="#23287a"/></svg>555-014-2288</p>
  <p class="abs contact c1"><span class="dot"></span>www.brookhollowfamilydentistry.example</p>
  <p class="abs contact c2"><span class="dot"></span>info@BrookhollowFamilyDentistry.example</p>

  <div class="abs photo" role="img" aria-label="Photo of a dentist giving a thumbs up beside a smiling young patient in the dental chair"></div>

  <p class="abs brand"><span class="mark"></span>BROOKHOLLOW FAMILY DENTISTRY</p>
  <p class="abs return">4270 Alder Crest Way,<br>Suite #101 Raleigh, NC 27613</p>
  <div class="abs stamp" aria-label="Stamp area"></div>
</section>

<section class="card card--front" aria-label="Postcard front">
  <svg class="shapes" viewBox="0 0 945 630" preserveAspectRatio="none" aria-hidden="true">
    <defs>
      <linearGradient id="front-green" x1="0" y1="0" x2="1" y2="0">
        <stop offset="0" stop-color="#5cb533"/><stop offset="1" stop-color="#3f9a2c"/>
      </linearGradient>
      <linearGradient id="tooth-photo" x1="0" y1="0" x2="1" y2="1">
        <stop offset="0" stop-color="#eef3f5"/><stop offset=".55" stop-color="#e9d2c4"/><stop offset="1" stop-color="#7fc4cf"/>
      </linearGradient>
    </defs>
    <g role="img" aria-label="Photo of a smiling dentist hugging a child, framed in a tooth outline">
      <path d="M60 70C120 30 190 60 245 90C300 60 380 30 430 60C475 90 460 200 430 280C400 360 360 420 330 430C300 420 290 330 245 310C200 330 190 420 160 430C130 420 90 360 70 280C40 200 20 100 60 70Z" fill="url(#tooth-photo)" stroke="#2e3192" stroke-width="9"/>
    </g>
    <path d="M0 505C150 470 300 470 470 500C650 530 820 480 945 395V630H0Z" fill="url(#front-green)"/>
    <path d="M0 488C150 455 260 455 330 472" fill="none" stroke="#2e3192" stroke-width="9"/>
    <path d="M600 522C760 512 870 462 945 412" fill="none" stroke="#2e3192" stroke-width="9"/>
  </svg>

  <p class="abs brand"><span class="mark"></span>BROOKHOLLOW<br>FAMILY DENTISTRY</p>
  <h1 class="abs headline"><span class="g">Personalized</span><span class="n">Modern Dentistry</span><span class="g">in Raleigh</span></h1>
  <p class="abs intro">We are a family dental office that provides <em>99%</em> of the dental service for the entire family</p>

  <div class="abs photo doctor" role="img" aria-label="Portrait photo of the dentist"></div>

  <p class="abs book">Book your next dental appointment</p>
  <p class="abs phone"><svg viewBox="0 0 24 24"><path d="M6.6 10.8a15 15 0 006.6 6.6l2.2-2.2c.3-.3.7-.4 1-.2 1.1.4 2.3.6 3.6.6.6 0 1 .4 1 1V20c0 .6-.4 1-1 1C10.6 21 3 13.4 3 4c0-.6.4-1 1-1h3.5c.6 0 1 .4 1 1 0 1.3.2 2.5.6 3.6.1.3 0 .7-.2 1z" fill="#23287a"/></svg>555-014-2288</p>

  <p class="abs contact c1">www.brookhollowfamilydentistry.example<span class="dot"></span></p>
  <p class="abs contact c2">info@BrookhollowFamilyDentistry.example<span class="dot"></span></p>
  <p class="abs contact c3">4270 Alder Crest Way, Suite #101 Raleigh, NC 27613<span class="dot"></span></p>
</section>

</body>
</html>
```